Morrow Engineering Core Values Branding Package

Morrow Engineering has recently refined its company Core Values and is seeking a strong, cohesive branding package to visually bring these values to life. The new graphic assets will communicate our commitment to excellence in a way that resonates with our team, clients, and partners in a blue-collar, industrial environment.

We are looking for multiple visual assets with consistent design elements that can be applied across platforms. The tone should reflect strength, reliability, and professionalism while remaining approachable and aligned with our industry.

Core Values & Descriptions
Accountability
“We take ownership of our work and actions, ensuring reliability and trust in every solution we deliver.”

Teamwork
“We collaborate across departments and disciplines to provide the highest level of service and innovation for our clients.”

Integrity
“We operate with honesty, transparency, and ethical standards in all aspects of our business.”

Growth
“We are committed to continuous improvement—of our people, our processes, and our impact in the industry.”

Deliverables

1. Primary Core Values Graphic
A master visual representing all four values together.
Designed for use on posters, office signage, internal presentations.

2. Individual Value Graphics (x4)
One graphic per core value: Accountability, Teamwork, Integrity, Growth.
Cohesive style with slight visual variation to reflect each value’s unique meaning.

Target Market(s)

Employees of Morrow Engineering

Industry/Entity Type

Blue Collar

Font styles to use
Sans Serif

Colors
0054AA
0677BA
7BADD7
CADEEF
E8F1F8
00AB8E
00BBA5
67D7C9
C6EFE9
E9F9F6
EB3D1F
EC4F4E
F09395
F8D3D4
FCEDEE

Requirements
Must have
• Accountability, Teamwork, Integrity, Growth

```html
<!DOCTYPE html>
<html lang="en">
<head>
<meta charset="utf-8">
<title>Morrow Engineering — Core Values</title>
<link rel="stylesheet" href="https://fonts.googleapis.com/css2?family=Roboto+Condensed:wght@400;700&display=swap">
<style>
  :root {
    --page-bg: #b4b4b4;
    --navy: #06306a;
    --green: #3db04b;
    --green-light: #8fd16a;
    --icon-top: rgba(61, 176, 75, 0.55);
    --icon-bottom: rgba(61, 176, 75, 0.18);
    --white: #ffffff;
    --rule: rgba(0, 0, 0, 0.35);
  }
  html, body {
    margin: 0;
    width: 1200px;
    height: 2434px;
    overflow: hidden;
    background: var(--page-bg);
  }
  .poster {
    position: absolute;
    left: 50px;
    top: 445px;
    width: 955px;
    height: 1340px;
    transform: scale(1.15183);
    transform-origin: 0 0;
    background: var(--navy);
    font-family: "Roboto Condensed", "Arial Narrow", sans-serif;
    color: var(--white);
    overflow: hidden;
  }
  .poster-art {
    position: absolute;
    inset: 0;
    width: 955px;
    height: 1340px;
  }
  .poster-title {
    font-family: "Roboto Condensed", "Arial Narrow", sans-serif;
    font-weight: 700;
    fill: var(--white);
  }
  .value {
    position: absolute;
    left: 442px;
    width: 500px;
  }
  .value-icon {
    position: absolute;
    left: 8px;
    top: 4px;
    width: 112px;
    height: 112px;
    border-radius: 14px;
    background: linear-gradient(160deg, var(--icon-top), var(--icon-bottom));
  }
  .value-text {
    position: absolute;
    left: 162px;
    top: 0;
    width: 350px;
  }
  .value-name {
    margin: 0;
    font-size: 40px;
    font-weight: 700;
    line-height: 42px;
    letter-spacing: 0.5px;
  }
  .value-desc {
    margin: 2px 0 0;
    font-size: 29px;
    font-weight: 400;
    line-height: 34.5px;
    letter-spacing: 0.2px;
    white-space: nowrap;
  }
  .value-rule {
    position: absolute;
    left: 462px;
    width: 440px;
    height: 3px;
    background: linear-gradient(90deg, transparent, var(--rule) 15%, var(--rule) 85%, transparent);
  }
  .brand-name {
    position: absolute;
    left: 455px;
    top: 1070px;
    width: 440px;
    margin: 0;
    text-align: center;
    font-weight: 700;
    color: var(--white);
    line-height: 1;
  }
  .brand-name .brand-main { display: block; font-size: 112px; letter-spacing: 2px; }
  .brand-name .brand-sub { display: block; font-size: 38px; letter-spacing: 9px; margin-top: 10px; }
</style>
</head>
<body>
<main class="poster">
  <svg class="poster-art" viewBox="0 0 955 1340" aria-hidden="true">
    <rect width="955" height="1340" fill="var(--navy)"/>
    <path class="green-panel" d="M0 0 H195 Q590 670 195 1340 H0 Z" fill="var(--green)"/>
    <path class="green-panel-line" d="M180 0 Q562 670 180 1340" fill="none" stroke="var(--green-light)" stroke-width="1.5" opacity="0.7"/>
    <path class="swoosh-top" d="M205 0 H242 Q335 115 382 305 Q312 118 205 0 Z" fill="var(--white)"/>
    <path class="swoosh-bottom" d="M384 1025 Q335 1235 238 1340 H198 Q318 1230 384 1025 Z" fill="var(--white)"/>
    <text class="poster-title" transform="translate(227 1190) rotate(-90)" font-size="225" textLength="1045" lengthAdjust="spacingAndGlyphs">CORE VALUE</text>
  </svg>

  <section class="value value-accountability" style="top:44px">
    <div class="value-icon" role="img" aria-label="Green line icon: document with check mark held in an open hand"></div>
    <div class="value-text">
      <h2 class="value-name">ACCOUNTABILITY</h2>
      <p class="value-desc">We take ownership of our<br>work and actions, ensuring<br>reliability and trust in every<br>solution we deliver.</p>
    </div>
  </section>
  <div class="value-rule" style="top:237px"></div>

  <section class="value value-teamwork" style="top:262px">
    <div class="value-icon" role="img" aria-label="Green line icon: team of people around a gear" style="top:10px"></div>
    <div class="value-text">
      <h2 class="value-name">TEAMWORK</h2>
      <p class="value-desc">We collaborate across<br>departments and disciplines<br>to provide the highest level<br>of service and innovation<br>for our clients.</p>
    </div>
  </section>
  <div class="value-rule" style="top:497px"></div>

  <section class="value value-integrity" style="top:527px">
    <div class="value-icon" role="img" aria-label="Green line icon: gear with circuit lines and an arrow" style="left:0"></div>
    <div class="value-text">
      <h2 class="value-name">INTEGRITY</h2>
      <p class="value-desc">We operate with honesty,<br>transparency, and<br>ethical standards in all<br>aspects of our business.</p>
    </div>
  </section>
  <div class="value-rule" style="top:722px"></div>

  <section class="value value-growth" style="top:764px">
    <div class="value-icon" role="img" aria-label="Green line icon: coin above a rising bar chart" style="top:6px"></div>
    <div class="value-text">
      <h2 class="value-name">GROWTH</h2>
      <p class="value-desc">We are committed to<br>continuous improvement—<br>of our people, our processes,<br>and our impact in the<br>industry.</p>
    </div>
  </section>

  <p class="brand-name"><span class="brand-main">MORROW</span><span class="brand-sub">ENGINEERING</span></p>
</main>
</body>
</html>
```